Business card for start up company

SIMPLE, CLEAN, FRESH, MODERN, SOPHISTICATED. professional. experienced, easy to deal with, expert in the field. local ethics.

professional business card for Forge Bay Industries. using company logo supplied and images.

GENERAL ENGINEERING - MACHINING - WELDING - MAINTENANCE

Forge Bay Industries Ltd is a locally owned mechanical engineering company that specialises in general and mechanical engineering, as well as steel fabrication, welding, repairs and maintenance.

We specialise in the design, welding, fabrication and installation of stainless and mild steel fabrications. We service commercial and residential clients; large or small projects; production line or one off designs.

We have built a solid reputation for quality and service for our machinery and engineering work around Northland NZ. For innovative, cost effective and efficient engineering solutions, to suit a wide range of commercial, residential and rural applications.

Target Market(s)

boat builders. DIY. industrial. RESIDENTIAL. COMMERCIAL

Industry/Entity Type

Mechanical Engineering

Contact Information for Business Card

CONTACT / SERVICES SIDE
Forge Bay Industries Ltd.
Design | Machining | Welding | Fabrication | Installation | Maintenance
www.forgebayindustries.example.nz
kevin@forgebayindustries.example.nz

Font styles to use
Serif

Colors

Designer to choose colors to be used in the design.

Requirements
Must have
• LOGO ONLY WITH NEGATIVE SPACE ON FRONT SIDE
• services and contact side , either use stock photos (supplied) as background or background supplied in logo photos.
Nice to have
• use the symbol icon in logo on contact/ services side, , enlarged, transparent and faded into the background with text over the top on the
• Design | Machining | Welding | Fabrication | Installation | Maintenance
• the above services to be subtle, along the bottom edge of the services side. can i also have another proof with eh above services featuring on the bottom edge of the LOGO FRONT side to see if the text looks better with or without.
Should not have
• crowded, busy, different fonts. different casing.
• use fonts in the logo files designer to make font decision.

```html
<!DOCTYPE html>
<html lang="en">
<head>
<meta charset="utf-8">
<title>Forge Bay Industries – Business Card</title>
<link href="https://fonts.googleapis.com/css2?family=Arimo:wght@400;700&display=swap" rel="stylesheet">
<style>
  :root {
    --page-bg: #d6d6d8;
    --card-dark: #0c0c0d;
    --card-mid: #2a2a2c;
    --card-sheen: #3a3a3c;
    --text-light: #e6e6e6;
    --text-soft: #d0d0d0;
    --accent: #e2501f;
    --band: rgba(0, 0, 0, 0.55);
  }
  * { margin: 0; padding: 0; box-sizing: border-box; }
  html, body {
    width: 1200px;
    height: 1000px;
    overflow: hidden;
  }
  body {
    background: var(--page-bg);
    font-family: "Arimo", Arial, sans-serif;
    position: relative;
  }
  .card {
    position: absolute;
    left: 304px;
    width: 593px;
    height: 347px;
    overflow: hidden;
    background: var(--card-dark);
  }
  .card--front { top: 136px; }
  .card--back { top: 518px; }

  .card__texture {
    position: absolute;
    inset: 0;
    background:
      radial-gradient(ellipse 60% 45% at 75% 30%, var(--card-sheen) 0%, transparent 70%),
      linear-gradient(155deg, var(--card-mid) 0%, #1a1a1b 35%, #232325 55%, var(--card-dark) 80%);
  }

  .brand {
    position: absolute;
    display: flex;
    align-items: center;
    gap: 10px;
    color: var(--text-light);
    font-weight: 700;
    text-transform: uppercase;
    white-space: nowrap;
  }
  .brand__mark {
    width: 11px;
    height: 11px;
    background: var(--accent);
    flex: none;
  }
  .card--front .brand {
    left: 50%;
    top: 50%;
    transform: translate(-50%, -50%);
    font-size: 26px;
    letter-spacing: 0.5px;
  }
  .card--back .brand {
    left: 75px;
    top: 73px;
    font-size: 32px;
    letter-spacing: 0.3px;
  }

  .contact-band {
    position: absolute;
    left: 0;
    top: 173px;
    width: 100%;
    height: 57px;
    background: var(--band);
    border-bottom: 2px solid var(--accent);
    padding: 12px 0 0 78px;
    color: var(--text-soft);
    font-size: 14px;
    line-height: 19px;
  }
  .services {
    position: absolute;
    left: 0;
    width: 100%;
    top: 299px;
    text-align: center;
    color: var(--text-soft);
    font-size: 14.5px;
    letter-spacing: 0.1px;
  }
</style>
</head>
<body>
  <section class="card card--front">
    <div class="card__texture" role="img" aria-label="Dark photographic background of curved ribbed steel surface"></div>
    <div class="brand">
      <span class="brand__name">Forge Bay Industries</span>
      <span class="brand__mark"></span>
    </div>
  </section>

  <section class="card card--back">
    <div class="card__texture" role="img" aria-label="Dark photographic background of curved ribbed steel surface"></div>
    <div class="brand">
      <span class="brand__mark"></span>
      <span class="brand__name">Forge Bay Industries</span>
    </div>
    <div class="contact-band">
      <p class="contact-band__web">www.forgebayindustries.example.nz</p>
      <p class="contact-band__email">kevin@forgebayindustries.example.nz</p>
    </div>
    <p class="services">Design | Machining | Welding | Fabrication | Installation | Maintenance</p>
  </section>
</body>
</html>
```